Divorce Lawyer print and ebook cover (Lanterns over the quiet harbor )

I need a front and back cover for my divorce and family law book. I already have a photo and title. The back cover photo is not necessary but can be interesting the Front-main cover is a must

Target Market(s)

Prospective client

Colors

Designer to choose colors to be used in the design.

Requirements
Must have
• Front photo by viewable.

```html
<!DOCTYPE html>
<html lang="en">
<head>
<meta charset="utf-8">
<title>Lanterns over the quiet harbor — Cover</title>
<link rel="stylesheet" href="https://fonts.googleapis.com/css2?family=Open+Sans:wght@400&family=PT+Serif:ital@1&display=swap">
<style>
  :root {
    --bg: #ecebe8;
    --band: #050505;
    --ink: #ffffff;
    --sub: #e6e2da;
    --badge-edge: #5a5a5a;
    --gold-a: #8a6a2c;
    --gold-b: #d9b766;
    --gold-c: #b48c3e;
    --name: #1a1408;
    --photo-sky: #b9cfd0;
    --photo-mid: #8d8876;
    --photo-ground: #6e6455;
  }
  html, body {
    margin: 0;
    width: 1200px;
    height: 1200px;
    overflow: hidden;
    background: var(--bg);
  }
  .cover {
    position: absolute;
    left: 236px;
    top: 40px;
    width: 728px;
    height: 1120px;
    background: var(--band);
    display: flex;
    flex-direction: column;
    box-shadow: 0 10px 30px rgba(0,0,0,0.18);
  }
  .cover-photo {
    height: 576px;
    background: linear-gradient(180deg, var(--photo-sky) 0%, #a8b4ac 30%, var(--photo-mid) 60%, var(--photo-ground) 100%);
  }
  .cover-text {
    flex: 1;
    display: flex;
    flex-direction: column;
    align-items: center;
    padding-top: 22px;
  }
  .title-main {
    margin: 0;
    font-family: "Open Sans", sans-serif;
    font-weight: 400;
    font-size: 86px;
    line-height: 1.05;
    color: var(--ink);
    letter-spacing: -1px;
  }
  .title-sub {
    margin: 0 0 28px;
    font-family: "Open Sans", sans-serif;
    font-weight: 400;
    font-size: 58px;
    line-height: 1.1;
    color: var(--ink);
  }
  .subtitle {
    margin: 0;
    font-family: "PT Serif", serif;
    font-style: italic;
    font-size: 36px;
    line-height: 1.2;
    color: var(--sub);
    text-align: center;
    transform: scaleX(0.86);
  }
  .store-badges {
    display: flex;
    gap: 10px;
    margin-top: 34px;
  }
  .store-badge {
    width: 160px;
    height: 50px;
    border: 1px solid var(--badge-edge);
    border-radius: 6px;
    background: var(--band);
  }
  .author-band {
    height: 67px;
    background: linear-gradient(180deg, var(--gold-a) 0%, var(--gold-b) 45%, var(--gold-c) 100%);
    display: flex;
    align-items: center;
    justify-content: center;
  }
  .author-name {
    font-family: "PT Serif", serif;
    font-style: italic;
    font-size: 44px;
    color: var(--name);
    letter-spacing: 2px;
  }
</style>
</head>
<body>
  <main class="cover">
    <div class="cover-photo" role="img" aria-label="Photo: a toddler in a teal knit hat on a playground swing, one parent's hand reaching in from each side"></div>
    <section class="cover-text">
      <h1 class="title-main">Lanterns over</h1>
      <p class="title-sub">the quiet harbor</p>
      <p class="subtitle">Practical Help for Your Divorce,<br>Child Custody or Alimony Case</p>
      <div class="store-badges">
        <div class="store-badge" aria-hidden="true"></div>
        <div class="store-badge" aria-hidden="true"></div>
      </div>
    </section>
    <footer class="author-band">
      <span class="author-name">NAME</span>
    </footer>
  </main>
</body>
</html>
```